White Cane Law Awareness Poster

Bright Harbor is a disability advocacy organization in Indiana. We are working on a project with the Cedarbrook Society of Staff for Low Sight. Our organizations need a design for a poster to promote awareness of Indiana's White Cane law. This poster will be displayed in local libraries, businesses, and other public places.

The poster should catch people's attention, and briefly explain that drivers have to yield for pedestrians who are blind who have white canes or seeing eye dogs.

The poster should be designed with people with low vision in mind. This means large text in a clear font, with good contrast between the text and the background. The text should be in a sans serif font that is clear and easy to read, with no italics or script fonts. There should not be a "busy" picture or pattern behind the text.

The poster should also include a reference to the relevant laws. We have attached a document with those references.

Finally, the poster should include the logos of Bright Harbor and the Cedarbrook Society of Staff for Low Sight, which we have included as attachments.

We have also included an attachment with a photo of the old White Cane Law poster, just to show an example of what we DO NOT want.

Industry/Entity Type

Non-Profit

Font styles to use
Sans Serif

Requirements
Must have
• The poster should also include a reference to the relevant laws. We have attached a document with those references.
• Finally, the poster should include the logos of Bright Harbor and the Cedarbrook Society of Staff for Low Sight, which we have included as attachments.

```html
<!DOCTYPE html>
<html lang="en">
<head>
<meta charset="utf-8">
<title>White Cane Law Awareness Poster</title>
<link rel="stylesheet" href="https://fonts.googleapis.com/css2?family=Roboto:wght@900&family=Roboto+Condensed:wght@700&display=swap">
<style>
  :root {
    --page-bg: #e9e9e9;
    --poster-red: #e0164a;
    --poster-red-light: #ea3f69;
    --headline-white: #ffffff;
    --law-yellow: #ffe01b;
    --logo-panel: #ffffff;
    --logo-ink: #1d2a5c;
  }
  * { margin: 0; padding: 0; box-sizing: border-box; }
  html, body {
    width: 1038px;
    height: 1200px;
    overflow: hidden;
    background: var(--page-bg);
  }
  .poster {
    position: absolute;
    left: 96px;
    top: 0;
    width: 846px;
    height: 1200px;
    background: var(--poster-red);
    overflow: hidden;
  }
  .hero-illustration {
    position: absolute;
    left: 177px;
    top: 27px;
    width: 532px;
    height: 443px;
    border-radius: 24px;
    background: linear-gradient(180deg, var(--poster-red) 0%, var(--poster-red-light) 100%);
  }
  .headline {
    position: absolute;
    left: 0;
    width: 100%;
    top: 480px;
    text-align: center;
    font-family: "Roboto", sans-serif;
    font-weight: 900;
    font-size: 178px;
    line-height: 1;
    letter-spacing: -4px;
    color: var(--headline-white);
  }
  .subhead {
    position: absolute;
    left: 0;
    width: 100%;
    top: 634px;
    text-align: center;
    font-family: "Roboto Condensed", sans-serif;
    font-weight: 700;
    font-size: 86px;
    line-height: 1;
    color: var(--law-yellow);
  }
  .law-text {
    position: absolute;
    left: 0;
    width: 100%;
    top: 724px;
    text-align: center;
    font-family: "Roboto Condensed", sans-serif;
    font-weight: 700;
    font-size: 48px;
    line-height: 56px;
    color: var(--headline-white);
  }
  .law-citation {
    position: absolute;
    left: 0;
    width: 100%;
    top: 1006px;
    text-align: center;
    font-family: "Roboto Condensed", sans-serif;
    font-weight: 700;
    font-size: 22px;
    line-height: 26px;
    letter-spacing: 1px;
    color: var(--law-yellow);
  }
  .partner-panel {
    position: absolute;
    left: 180px;
    top: 1043px;
    width: 484px;
    height: 155px;
    background: var(--logo-panel);
    display: flex;
    align-items: center;
    justify-content: space-around;
    padding: 0 18px;
  }
  .partner {
    display: flex;
    align-items: center;
    gap: 10px;
    font-family: "Roboto Condensed", sans-serif;
    font-weight: 700;
    color: var(--logo-ink);
  }
  .partner-mark {
    flex: none;
    width: 34px;
    height: 34px;
    border-radius: 50%;
    background: var(--logo-ink);
  }
  .partner-name--harbor { font-size: 26px; line-height: 1.1; }
  .partner-name--cedarbrook { font-size: 17px; line-height: 1.15; width: 170px; }
</style>
</head>
<body>
  <main class="poster">
    <div class="hero-illustration" role="img" aria-label="Illustration of a blind pedestrian with a white cane and a guide dog on a harness, with two small clouds"></div>

    <h1 class="headline">STOP!</h1>
    <p class="subhead">IT’S THE LAW!</p>
    <p class="law-text">
      DRIVERS SHALL<br>
      YIELD THE RIGHT-OF-WAY<br>
      TO A BLIND PEDESTRIAN CARRYING<br>
      A CLEARLY VISIBLE WHITE CANE<br>
      OR ACCOMPANIED BY A GUIDE DOG.
    </p>
    <p class="law-citation">INDIANA CODE 9-21-17-21 · WHITE CANE LAW</p>

    <footer class="partner-panel">
      <div class="partner">
        <span class="partner-mark" aria-hidden="true"></span>
        <span class="partner-name partner-name--harbor">Bright Harbor</span>
      </div>
      <div class="partner">
        <span class="partner-name partner-name--cedarbrook">Cedarbrook Society of Staff for Low Sight</span>
      </div>
    </footer>
  </main>
</body>
</html>
```